Load Up Your Cart

Require two banners with a size of 980 x 450 pixels
Similar natural looking banner as per attachment. The background is supposed to be a cardboard carton
price "$9.95"
Wording and layout the same as attached file

```html
<!DOCTYPE html>
<html lang="en">
<head>
<meta charset="utf-8">
<title>Load Up Your Cart – Flat Rate Shipping</title>
<link rel="stylesheet" href="https://fonts.googleapis.com/css2?family=Anton&family=Josefin+Sans:wght@300&family=Stardos+Stencil:wght@700&display=swap">
<style>
  :root {
    --bg-light: #ffe08e;
    --bg-mid: #fdd46a;
    --bg-dark: #f8c24a;
    --ring: #3d2d1b;
    --circle-text: #6b5535;
    --price-red: #f2102a;
    --stencil-dark: #46361f;
    --stencil-mid: #6e5a3c;
  }
  html, body {
    margin: 0;
    padding: 0;
    width: 1200px;
    height: 551px;
    overflow: hidden;
  }
  .banner {
    display: block;
    width: 1200px;
    height: 551px;
  }
  .circle-word {
    font-family: "Josefin Sans", sans-serif;
    font-weight: 300;
    fill: var(--circle-text);
  }
  .price {
    font-family: "Anton", sans-serif;
    fill: var(--price-red);
  }
  .headline {
    font-family: "Stardos Stencil", serif;
    font-weight: 700;
    fill: var(--stencil-dark);
  }
  .tagline {
    font-family: "Stardos Stencil", serif;
    font-weight: 700;
    fill: var(--stencil-mid);
  }
</style>
</head>
<body>
<svg class="banner" viewBox="0 0 980 450" xmlns="http://www.w3.org/2000/svg" role="img" aria-label="Load up your cart – $9,95 flat rate shipping">
  <defs>
    <radialGradient id="warm-glow" cx="620" cy="190" r="620" gradientUnits="userSpaceOnUse">
      <stop offset="0" stop-color="var(--bg-light)"/>
      <stop offset="0.55" stop-color="var(--bg-mid)"/>
      <stop offset="1" stop-color="var(--bg-dark)"/>
    </radialGradient>
  </defs>

  <rect class="backdrop" width="980" height="450" fill="url(#warm-glow)"/>

  <g class="cart-badge">
    <circle cx="228" cy="233" r="205" fill="none" stroke="var(--ring)" stroke-width="14"/>
    <g transform="rotate(-8 228 233)">
      <text class="circle-word" x="88" y="210" font-size="100" textLength="268" lengthAdjust="spacingAndGlyphs">LOAD</text>
      <text class="circle-word" x="98" y="335" font-size="104" textLength="118" lengthAdjust="spacingAndGlyphs">UP</text>
      <text class="circle-word" x="236" y="266" font-size="46" textLength="120" lengthAdjust="spacingAndGlyphs">YOUR</text>
      <text class="circle-word" x="244" y="322" font-size="46" textLength="122" lengthAdjust="spacingAndGlyphs">CART</text>
    </g>
  </g>

  <text class="price" x="572" y="200" font-size="138" textLength="256" lengthAdjust="spacingAndGlyphs">$9,95</text>
  <text class="headline" x="440" y="325" font-size="54" textLength="495" lengthAdjust="spacingAndGlyphs">FLAT RATE SHIPPING</text>
  <text class="tagline" x="383" y="400" font-size="38" textLength="592" lengthAdjust="spacingAndGlyphs">NO MINIMUMS. NO CODES. NO GIMMICKS.</text>
</svg>
</body>
</html>
```